Harbor Fresh Cleaning car wrap

I need a car wrap design for my work van that is eye catching and stands out. My type of business is carpet cleaning and tile and grout cleaning along with other services. I would like the services to be listed on the wrap along with the phone number and website.
Also please add that we service Commercial and Residential.
Website is:
HarborFreshCleaning.example
Phone number (555) 304-2917
The services I provide are as follow:
Tile & Grout Cleaning
Carpet Cleaning
Hardwood Floor Cleaning and Refinishing
Upholstery and Rug Cleaning
My business colors consist of blue and white but I am open to using other colors.
My logo is attached in the files.
Commercial and Residential
Carpet Cleaning

```html
<!DOCTYPE html>
<html lang="en">
<head>
<meta charset="utf-8">
<title>Harbor Fresh Cleaning – Van Wrap</title>
<link rel="stylesheet" href="https://fonts.googleapis.com/css2?family=Oswald:wght@500;600;700&display=swap">
<style>
  :root {
    --teal: #0f8a85;
    --teal-dark: #0b716d;
    --white: #ffffff;
    --ink: #1e1f21;
    --stage: #eceff0;
  }
  * { box-sizing: border-box; margin: 0; padding: 0; }
  html, body { width: 1200px; height: 800px; overflow: hidden; }
  body {
    background: var(--stage);
    font-family: "Oswald", "Arial Narrow", sans-serif;
    position: relative;
    text-transform: uppercase;
  }

  /* ---------- side panel ---------- */
  .wrap-side {
    position: absolute; left: 40px; top: 30px;
    width: 1120px; height: 380px;
    background: var(--white);
    border-radius: 18px;
    overflow: hidden;
    box-shadow: 0 2px 10px rgba(0,0,0,.08);
  }
  .wrap-side .sweep { position: absolute; inset: 0; }
  .brand-name {
    font-weight: 700; color: var(--teal);
    line-height: 1; letter-spacing: .5px;
  }
  .side-brand { position: absolute; left: 320px; top: 70px; font-size: 34px; }
  .side-brand span { display: block; }
  .side-call {
    position: absolute; left: 260px; top: 250px;
    font-weight: 600; font-size: 25px; line-height: 1.35; color: var(--ink);
  }
  .side-call .phone { color: var(--teal); }
  .web-pill {
    background: var(--white); color: var(--ink);
    font-weight: 600; letter-spacing: 2px;
    border-radius: 999px;
    display: flex; align-items: center;
  }
  .side-web {
    position: absolute; left: 570px; top: 48px;
    width: 470px; height: 52px; padding-left: 34px; font-size: 27px;
  }
  .services { position: absolute; left: 640px; top: 120px; color: var(--white); }
  .services h2 { font-weight: 700; font-size: 32px; letter-spacing: 1px; margin-bottom: 10px; }
  .services ul { list-style: none; font-weight: 500; font-size: 17px; line-height: 1.55; }
  .services li::before { content: "-"; }
  .services .cont { padding-left: 8px; }
  .side-divider {
    position: absolute; left: 875px; top: 150px;
    width: 2px; height: 130px; background: var(--white);
  }
  .side-badge {
    position: absolute; left: 905px; top: 175px;
    display: flex; align-items: center; gap: 12px;
  }
  .side-badge .dot { width: 22px; height: 22px; border-radius: 50%; background: var(--white); }
  .side-badge .brand-name { color: var(--white); font-size: 31px; }
  .side-badge .brand-name span { display: block; }

  /* ---------- rear panel ---------- */
  .wrap-rear {
    position: absolute; left: 430px; top: 435px;
    width: 340px; height: 345px;
    background: var(--teal);
    border-radius: 22px 22px 10px 10px;
    color: var(--white);
    text-align: center;
    box-shadow: 0 2px 10px rgba(0,0,0,.08);
  }
  .rear-web {
    margin: 18px auto 0; width: 290px; height: 32px;
    justify-content: center; font-size: 16px; letter-spacing: 1px;
  }
  .rear-brand {
    color: var(--white); font-size: 32px; margin-top: 22px;
  }
  .rear-brand span { display: block; }
  .rear-tag { font-weight: 600; font-size: 21px; margin-top: 26px; }
  .rear-phone { font-weight: 600; font-size: 34px; margin-top: 4px; letter-spacing: .5px; }
  .rear-points {
    list-style: none; text-align: left; display: inline-block;
    font-weight: 500; font-size: 17px; line-height: 1.6; margin-top: 12px;
  }
  .rear-points li::before { content: "• "; }
</style>
</head>
<body>

  <section class="wrap-side" aria-label="Van side wrap">
    <svg class="sweep" width="1120" height="380" viewBox="0 0 1120 380" aria-hidden="true">
      <path d="M640,0 H1120 V380 H420 C520,335 565,230 578,110 Q586,0 640,0 Z" fill="var(--teal)"/>
    </svg>

    <div class="brand-name side-brand"><span>Harbor Fresh</span><span>Cleaning</span></div>

    <p class="side-call">Refresh your floors<br>today : <span class="phone">(555) 304-2917</span></p>

    <div class="web-pill side-web">HarborFreshCleaning.example</div>

    <div class="services">
      <h2>Services:</h2>
      <ul>
        <li>Tile &amp; Grout Cleaning</li>
        <li>Carpet Cleaning</li>
        <li>Hardwood Floor Cleaning<br><span class="cont">and Refinishing</span></li>
        <li>Upholstery and Rug Cleaning</li>
      </ul>
    </div>

    <div class="side-divider"></div>

    <div class="side-badge">
      <div class="dot"></div>
      <div class="brand-name"><span>Harbor Fresh</span><span>Cleaning</span></div>
    </div>
  </section>

  <section class="wrap-rear" aria-label="Van rear wrap">
    <div class="web-pill rear-web">HarborFreshCleaning.example</div>
    <div class="brand-name rear-brand"><span>Harbor Fresh</span><span>Cleaning</span></div>
    <p class="rear-tag">Refresh your floors today!</p>
    <p class="rear-phone">(555) 304-2917</p>
    <ul class="rear-points">
      <li>Commercial &amp; Residential</li>
      <li>Licensed &amp; Insured</li>
    </ul>
  </section>

</body>
</html>
```